Live Webcasting Host Wants Template/Theme to Jumpstare Ecommerce Site

Please,Please, Please READ ALL OF THE DESCRIPTION. Thank you.

I need a template for a look for my developer to work with in designing an ecommerce site where clients pay a monthly fee for streaming services and video on demand.

I'll need 2 pages designed:
1) public page
2) client log in landing page.

Please use a CMS (WP preferred) as this will allow is for further content to be added after delivery. Please include the pricing text in boxes in slides (pdf) to help fill out you design for the home page.

The attached slides are to give you a general layout of how I envision the pages. Yes I would like the Client page to be tabbed from the side like in the attached slide.

I've attached company logos for use along with the accompanying .psd and .ai files in the zip. Use the colors in logo in site design.

Thank you for your time.
Updates

Please, no designs. This is for a CMS for webpage design like WordPress or Joomla. Thanks. Added Friday, January 13, 2017

Reason: Looking for more designs.

Target Market(s)

Churches, Organizations, Civic Organizations, Government Agencies (State, Local) -BUT don't let this deter your creativity. Decision makers/influencers will be video production and/or IT personnel.

Industry/Entity Type

It Company

Font styles to use
Sans Serif

Colors
f5f5f5
e8e8e8
333333
fece3e
cbcbcb
33a6d7
000000

Requirements
Must have
• Responsive Design
Nice to have
• One Page Design
Should not have
• SHOULD NOT HAVE White overall background but use white in other ways if you like.

```html
<!DOCTYPE html>
<html lang="en">
<head>
<meta charset="utf-8">
<title>Vidora – Live Video Hosting</title>
<link rel="stylesheet" href="https://fonts.googleapis.com/css2?family=Lato:wght@300;400;700;900&display=swap">
<style>
:root{
  --yellow:#fece3e;
  --orange:#f7a21b;
  --ink:#222222;
  --text:#333333;
  --muted:#8a8f96;
  --band:#eeeeee;
  --band-light:#f2f2f2;
  --white:#ffffff;
  --side:#242424;
  --blue:#1e7fc0;
  --teal:#1fbe9a;
  --track:#eeeeee;
}
*{box-sizing:border-box;margin:0;padding:0}
html,body{width:1200px;height:960px;overflow:hidden}
body{font-family:'Lato',sans-serif;color:var(--text);background:var(--white);position:relative}
.abs{position:absolute}

/* header */
.site-header{position:absolute;left:0;top:0;width:1200px;height:125px;background:var(--white)}
.brand-box{position:absolute;left:85px;top:0;width:280px;height:125px;background:var(--yellow);display:flex;flex-direction:column;align-items:center;justify-content:center}
.brand-name{font-weight:900;font-size:44px;letter-spacing:1px;color:var(--ink);line-height:1}
.brand-tag{font-size:12px;font-weight:700;letter-spacing:2px;color:var(--ink);margin-top:8px}
.login-btn{position:absolute;left:974px;top:18px;width:144px;height:44px;border-radius:22px;background:#111;display:flex;align-items:center;color:var(--white);font-weight:900;font-size:20px;letter-spacing:1.5px}
.login-btn .icon{width:44px;height:44px;background:var(--orange);border-radius:6px;display:flex;align-items:center;justify-content:center;margin-right:10px}
.main-nav{position:absolute;top:86px;left:0;width:1200px;height:22px;font-size:16px;color:var(--ink)}
.main-nav span{position:absolute;top:0;white-space:nowrap}
.main-nav .home{left:496px;top:-6px}

/* showcase band */
.showcase{position:absolute;left:0;top:125px;width:1200px;height:583px;background:var(--band)}

/* dashboard */
.dash{position:absolute;left:86px;top:171px;width:1041px;height:537px;background:#f3f3f3;overflow:hidden;border-top:2px solid #ccc}
.dash-side{position:absolute;left:0;top:0;width:129px;height:537px;background:var(--side)}
.side-active{position:absolute;left:0;top:10px;width:129px;height:27px;background:var(--blue);color:var(--white);font-size:13px;display:flex;align-items:center;padding-left:8px;gap:7px}
.side-active::after{content:"";position:absolute;right:0;top:8px;border:6px solid transparent;border-right-color:#f3f3f3}
.side-item{position:absolute;left:8px;color:#e8e8e8;font-size:14px;display:flex;align-items:center;gap:9px}
.side-item i{display:block;width:12px;height:11px;background:#888;border-radius:2px}
.dash-top{position:absolute;left:129px;top:0;width:904px;height:45px;background:#f0f0f0;border-bottom:1px solid #e0e0e0}
.burger{position:absolute;left:19px;top:16px;width:16px}
.burger i{display:block;height:2px;background:#444;margin-bottom:3px}
.mail{position:absolute;left:783px;top:18px;width:11px;height:9px;border:1.5px solid #555;border-radius:1px}
.mail-badge{position:absolute;left:792px;top:9px;width:12px;height:12px;border-radius:50%;background:var(--teal);color:#fff;font-size:7px;text-align:center;line-height:12px}
.avatar{position:absolute;left:814px;top:11px;width:21px;height:21px;border-radius:50%;background:#c9c9c9}
.user-name{position:absolute;left:839px;top:16px;font-size:10px;color:#333;font-weight:700}
.scrollbar{position:absolute;left:1033px;top:2px;width:8px;height:507px;background:#000}

.stats{position:absolute;left:129px;top:45px;width:904px;height:80px}
.stat{position:absolute;top:0;width:148px;height:80px;padding-left:37px}
.stat .label{font-size:9.5px;color:var(--muted);margin-top:13px;white-space:nowrap}
.stat .num{font-size:29px;color:#555;line-height:34px;font-weight:400}
.stat .num.teal{color:var(--teal)}
.stat .sub{font-size:9px;color:var(--muted);white-space:nowrap}
.stat .sub b{color:var(--teal);font-weight:400;font-style:italic}
.stat .sub b.down{color:#e0483e}
.stat-div{position:absolute;top:16px;width:1px;height:48px;background:#ccc}

.card{position:absolute;background:var(--white);overflow:hidden}
.chart-card{left:144px;top:129px;width:872px;height:250px}
.card-head{position:absolute;left:0;top:0;right:0;height:37px;border-bottom:2px solid #f0f0f0}
.card-title{position:absolute;left:12px;top:10px;font-size:17px;color:#555;font-weight:400}
.card-title small{font-size:11px;color:#666}
.date-pill{position:absolute;right:12px;top:8px;width:206px;height:22px;border:1px solid #ddd;font-size:9px;color:#999;line-height:20px;padding-left:8px}
.camp-title{position:absolute;left:654px;top:54px;font-size:13px;color:#666;width:208px;padding-bottom:7px;border-bottom:1px solid #e6e6e6}
.camp{position:absolute;left:658px;width:150px;font-size:9px;color:#777}
.track{height:6px;background:var(--track);margin-top:6px;position:relative}
.track i{position:absolute;left:0;top:0;bottom:0;background:var(--teal)}

.mini{top:391px;width:280px;height:170px}
.mini .card-head{left:16px;right:16px;height:38px;border-bottom:2px solid #eee}
.mini .card-title{left:6px;top:12px;font-size:13.5px}
.tools{position:absolute;right:6px;top:16px;font-size:9px;color:#bbb;letter-spacing:6px}
.row{position:absolute;font-size:10px;color:#555}
.bar{position:absolute;height:14px;background:var(--track)}
.bar i{position:absolute;left:0;top:0;bottom:0;background:var(--teal)}
.big-val{position:absolute;font-size:15px;color:#555}
.swatch{position:absolute;width:10px;height:10px}
.profile-box{position:absolute;left:139px;top:63px;width:123px;height:120px;border:1px solid #cde7f3;border-radius:2px}
.profile-box p{font-size:11.5px;color:#555;text-align:center;margin-top:10px}

/* newsletter */
.newsletter{position:absolute;left:0;top:708px;width:1200px;height:116px;background:var(--band-light)}
.nl-label{position:absolute;left:194px;top:46px;display:flex;align-items:center;gap:14px;font-size:16.5px;letter-spacing:0.6px;color:#333;white-space:nowrap}
.nl-input{position:absolute;left:541px;top:34px;width:330px;height:44px;background:var(--white);font-size:12px;color:#ccc;line-height:44px;padding-left:4px}
.nl-btn{position:absolute;left:888px;top:34px;width:123px;height:44px;background:var(--orange);color:#222;font-size:16px;letter-spacing:1px;text-align:center;line-height:44px}

/* footer */
.site-footer{position:absolute;left:0;top:824px;width:1200px;height:136px;background:var(--white)}
.foot-brand{position:absolute;left:86px;top:50px;display:flex;flex-direction:column;align-items:center}
.foot-brand .brand-name{font-size:40px}
.foot-brand .brand-tag{font-size:11px;margin-top:6px}
.legal{position:absolute;left:310px;top:71px;font-size:18px;letter-spacing:0.5px;color:#333}
.social{position:absolute;top:64px;width:34px;height:34px;border-radius:50%;background:#333}
.to-top{position:absolute;left:1117px;top:95px;width:41px;height:41px;background:var(--orange);display:flex;align-items:center;justify-content:center}
</style>
</head>
<body>

<header class="site-header">
  <div class="brand-box">
    <div class="brand-name">VIDORA</div>
    <div class="brand-tag">LIVE VIDEO HOSTING</div>
  </div>
  <div class="login-btn">
    <span class="icon">
      <svg width="26" height="26" viewBox="0 0 26 26"><circle cx="12" cy="8" r="5" fill="#111"/><path d="M3 24c0-6 4-9 9-9s9 3 9 9z" fill="#111"/><circle cx="20" cy="19" r="4" fill="#fff"/><path d="M18 19l1.5 1.5L22 18" stroke="#111" stroke-width="1.3" fill="none"/></svg>
    </span>LOGIN
  </div>
  <nav class="main-nav">
    <span class="home"><svg width="24" height="22" viewBox="0 0 24 22"><path d="M12 1L1 11h3v10h6v-6h4v6h6V11h3z" fill="#f7a21b"/></svg></span>
    <span style="left:552px">FEATURES</span>
    <span style="left:666px">PRICING</span>
    <span style="left:765px">ABOUT US</span>
    <span style="left:880px">WEBCASTING 101</span>
    <span style="left:1043px">CONTACT</span>
  </nav>
</header>

<section class="showcase"></section>

<div class="dash">
  <aside class="dash-side">
    <div class="side-active"><svg width="12" height="11" viewBox="0 0 12 11"><path d="M6 0L0 5h2v6h3V7h2v4h3V5h2z" fill="#fff"/></svg>Dashboard</div>
    <div class="side-item" style="top:51px"><i></i>Account</div>
    <div class="side-item" style="top:84px"><i></i>Player</div>
    <div class="side-item" style="top:114px"><i></i>Analytics</div>
    <div class="side-item" style="top:146px"><i></i>Support</div>
  </aside>

  <div class="dash-top">
    <div class="burger"><i></i><i></i><i></i></div>
    <div class="mail"></div>
    <div class="mail-badge">6</div>
    <div class="avatar"></div>
    <div class="user-name">Alex Rowe ⌄</div>
  </div>
  <div class="scrollbar"></div>

  <div class="stats">
    <div class="stat" style="left:0"><div class="label">Total Users</div><div class="num">2500</div><div class="sub"><b>4%</b> From last Week</div></div>
    <div class="stat-div" style="left:157px"></div>
    <div class="stat" style="left:148px"><div class="label">Avarare Time</div><div class="num">123.50</div><div class="sub"><b>3%</b> From last Week</div></div>
    <div class="stat-div" style="left:304px"></div>
    <div class="stat" style="left:295px"><div class="label">Total Males</div><div class="num teal">2,500</div><div class="sub"><b>34%</b> From last Week</div></div>
    <div class="stat-div" style="left:451px"></div>
    <div class="stat" style="left:443px"><div class="label">Total Females</div><div class="num">4,567</div><div class="sub"><b class="down">12%</b> From last Week</div></div>
    <div class="stat-div" style="left:599px"></div>
    <div class="stat" style="left:590px"><div class="label">Total Collections</div><div class="num">2,315</div><div class="sub"><b>34%</b> From last Week</div></div>
    <div class="stat-div" style="left:747px"></div>
    <div class="stat" style="left:738px"><div class="label">Total Connections</div><div class="num">7,325</div><div class="sub"><b>34%</b> From last Week</div></div>
  </div>

  <section class="card chart-card">
    <div class="card-head">
      <div class="card-title">Network Activities <small>Graph title sub-title</small></div>
      <div class="date-pill">October 25, 2015 - November 23, 2015 ▾</div>
    </div>
    <svg class="abs" style="left:0;top:0" width="650" height="250" viewBox="0 0 650 250" aria-label="Network activity area chart" font-family="Lato, sans-serif" font-size="8" fill="#555">
      <g stroke="#eee" stroke-width="1">
        <line x1="26" y1="50" x2="26" y2="228"/><line x1="136" y1="50" x2="136" y2="228"/>
        <line x1="238" y1="50" x2="238" y2="228"/><line x1="340" y1="50" x2="340" y2="228"/>
        <line x1="440" y1="50" x2="440" y2="228"/><line x1="542" y1="50" x2="542" y2="228"/>
      </g>
      <g text-anchor="end">
        <text x="22" y="53">130</text><text x="22" y="67">120</text><text x="22" y="80">110</text>
        <text x="22" y="94">100</text><text x="22" y="108">90</text><text x="22" y="121">80</text>
        <text x="22" y="135">70</text><text x="22" y="149">60</text><text x="22" y="162">50</text>
        <text x="22" y="176">40</text><text x="22" y="190">30</text><text x="22" y="203">20</text>
        <text x="22" y="217">10</text><text x="22" y="231">0</text>
      </g>
      <path d="M26,118 C60,170 80,201 100,201 C150,201 190,139 230,139 C270,139 290,201 314,201 C360,201 395,64 432,64 C470,64 480,228 506,228 L636,222 L636,228 L26,228Z" fill="#7fa3b0" fill-opacity="0.8"/>
      <path d="M26,180 C60,150 100,125 136,125 C180,125 200,205 240,205 C280,205 290,173 322,173 C360,173 380,212 420,200 C470,170 490,112 540,112 C590,112 620,190 636,215 L636,228 L26,228Z" fill="#8fdcc6" fill-opacity="0.75"/>
      <line x1="26" y1="228" x2="636" y2="228" stroke="#ccc"/>
      <g text-anchor="middle">
        <text x="34" y="240">Jan 01</text><text x="136" y="240">Jan 02</text><text x="238" y="240">Jan 03</text>
        <text x="340" y="240">Jan 04</text><text x="440" y="240">Jan 05</text><text x="542" y="240">Jan 06</text>
      </g>
    </svg>
    <div class="camp-title">Top Campaign Performance</div>
    <div class="camp" style="top:86px">Social Campaign<div class="track"><i style="width:80%"></i></div></div>
    <div class="camp" style="top:123px">Microblog Campaign<div class="track"><i style="width:60%"></i></div></div>
    <div class="camp" style="top:161px">Conventional Media<div class="track"><i style="width:40%"></i></div></div>
    <div class="camp" style="top:198px">Bill boards<div class="track"><i style="width:50%"></i></div></div>
  </section>

  <section class="card mini" style="left:144px">
    <div class="card-head"><div class="card-title">App Versions</div><div class="tools">^ ⁄ ×</div></div>
    <div class="row" style="left:16px;top:56px;font-size:12px">App Usage across versions</div>
    <div class="row" style="left:16px;top:78px">0.1.5.2</div>
    <div class="bar" style="left:78px;top:77px;width:134px"><i style="width:66%"></i></div>
    <div class="big-val" style="left:229px;top:75px">123k</div>
    <div class="row" style="left:16px;top:107px">0.1.5.3</div>
    <div class="bar" style="left:78px;top:106px;width:134px"><i style="width:44%"></i></div>
    <div class="big-val" style="left:237px;top:104px">53k</div>
    <div class="row" style="left:16px;top:137px">0.1.5.4</div>
    <div class="bar" style="left:78px;top:136px;width:134px"><i style="width:25%"></i></div>
    <div class="big-val" style="left:237px;top:134px">23k</div>
  </section>

  <section class="card mini" style="left:440px">
    <div class="card-head"><div class="card-title">Device Usage</div><div class="tools">^ ⁄ ×</div></div>
    <div class="row" style="left:16px;top:51px;font-weight:700;font-size:9px">Top 5</div>
    <div class="row" style="left:132px;top:51px;font-weight:700;font-size:9px">Device</div>
    <div class="row" style="left:213px;top:51px;font-weight:700;font-size:9px">Progress</div>
    <svg class="abs" style="left:16px;top:80px" width="100" height="100" viewBox="0 0 100 100" aria-label="Device usage donut chart">
      <g fill="none" stroke-width="20">
        <circle cx="50" cy="50" r="40" stroke="#3498db" stroke-dasharray="150 251" transform="rotate(-180 50 50)"/>
        <circle cx="50" cy="50" r="40" stroke="#455a6e" stroke-dasharray="25 251" transform="rotate(-90 50 50)"/>
        <circle cx="50" cy="50" r="40" stroke="#9b59b6" stroke-dasharray="25 251" transform="rotate(-54 50 50)"/>
        <circle cx="50" cy="50" r="40" stroke="#bdc3c7" stroke-dasharray="50 251" transform="rotate(-18 50 50)"/>
      </g>
    </svg>
    <div class="swatch" style="left:132px;top:84px;background:#3498db"></div>
    <div class="row" style="left:148px;top:82px;font-size:11px">Orbit OS</div>
    <div class="row" style="left:253px;top:82px;font-size:11px">30%</div>
    <div class="swatch" style="left:132px;top:106px;background:var(--teal)"></div>
    <div class="row" style="left:148px;top:104px;font-size:11px">Droidix</div>
    <div class="row" style="left:253px;top:104px;font-size:11px">10%</div>
    <div class="swatch" style="left:132px;top:128px;background:#9b59b6"></div>
    <div class="row" style="left:148px;top:126px;font-size:11px">Berrytel</div>
    <div class="row" style="left:253px;top:126px;font-size:11px">20%</div>
  </section>

  <section class="card mini" style="left:736px">
    <div class="card-head"><div class="card-title">Quick Settings</div><div class="tools">^ ⁄ ×</div></div>
    <div class="row" style="left:23px;top:59px">▫ Settings</div>
    <div class="row" style="left:23px;top:81px">≡ Subscription</div>
    <div class="row" style="left:23px;top:102px">▥ Auto Renewal</div>
    <div class="row" style="left:23px;top:123px">⟋ Achievements</div>
    <div class="profile-box">
      <p>Profile Completion</p>
      <svg class="abs" style="left:20px;top:36px" width="84" height="84" viewBox="0 0 84 84" aria-label="Profile completion gauge">
        <circle cx="42" cy="42" r="32" fill="none" stroke="#eee" stroke-width="16"/>
        <path d="M10 42 A32 32 0 0 1 60 15" fill="none" stroke="var(--teal)" stroke-width="16"/>
        <line x1="42" y1="48" x2="56" y2="14" stroke="#222" stroke-width="2"/>
      </svg>
    </div>
  </section>
</div>

<section class="newsletter">
  <div class="nl-label">
    <svg width="26" height="18" viewBox="0 0 26 18"><rect width="26" height="18" fill="#f7a21b"/><path d="M0 0l13 10L26 0" fill="none" stroke="#fff" stroke-width="1.5"/></svg>
    SUBCRIBE TO OUR NEWSLETTER
  </div>
  <div class="nl-input">YOUR EMAIL ADDRESS</div>
  <div class="nl-btn">SUBCRIBE</div>
</section>

<footer class="site-footer">
  <div class="foot-brand">
    <div class="brand-name">VIDORA</div>
    <div class="brand-tag">LIVE VIDEO HOSTING</div>
  </div>
  <div class="legal">© 2017 | PRIVACY POLICY</div>
  <span class="social" style="left:948px" aria-label="Social link"></span>
  <span class="social" style="left:990px" aria-label="Feed link"></span>
  <span class="social" style="left:1033px" aria-label="Social link"></span>
  <span class="social" style="left:1074px" aria-label="Social link"></span>
  <div class="to-top"><svg width="18" height="10" viewBox="0 0 18 10"><path d="M1 9L9 1l8 8" fill="none" stroke="#fff" stroke-width="1.5"/></svg></div>
</footer>

</body>
</html>
```